We need a web page design for a new company called "Quarry". We provide an innovative music sharing mobile application that allows music listeners to share their music without paying for a monthly subscription. We would like to incorporate the attached logo and color scheme. The final design should communicate music gifting and sharing.

Industry/Entity Type

It Company

```html
<!DOCTYPE html>
<html lang="en">
<head>
<meta charset="utf-8">
<title>Quarry</title>
<link rel="stylesheet" href="https://fonts.googleapis.com/css2?family=Roboto:ital,wght@0,400;0,500;0,700;1,700&family=Lato:wght@400;700&display=swap">
<style>
:root{
  --green:#68a81e;
  --green-light:#8cbf48;
  --orange:#f7941d;
  --orange-dark:#f08a0c;
  --grey-btn:#a3a3a3;
  --text:#333;
  --cream:#ece7d8;
  --cream-line:#d9d3c1;
  --footer:#333333;
  --footer-deep:#262626;
  --white:#fff;
}
*{margin:0;padding:0;box-sizing:border-box}
html,body{width:821px;height:1200px;overflow:hidden;background:var(--white)}
body{position:relative;font-family:"Roboto",Arial,sans-serif;color:var(--text)}
.abs{position:absolute}

/* header */
.site-header{position:absolute;left:0;top:0;width:821px;height:60px;background:var(--green)}
.brand{position:absolute;left:119px;top:14px;display:flex;align-items:center;gap:6px;color:var(--white)}
.brand-dot{width:28px;height:28px;border-radius:50%;background:var(--white)}
.brand-name{font-family:"Lato",sans-serif;font-weight:700;font-size:29px;line-height:30px}
.main-nav a{position:absolute;top:33px;font-size:9px;font-weight:700;color:var(--white);text-decoration:none;letter-spacing:.2px}
.main-nav .active{top:0;left:379px;width:43px;height:60px;background:var(--white);color:var(--text);display:flex;align-items:center;justify-content:center;padding-top:16px}
.account{position:absolute;right:77px;top:13px;font-size:8px;color:var(--white);letter-spacing:.3px}

/* hero */
.hero{position:absolute;left:0;top:60px;width:821px;height:263px;background:linear-gradient(100deg,#5a5550 0%,#8a7f74 28%,#c9b7a3 48%,#e6dcd2 70%,#b9aea4 100%)}

/* features */
.feature{position:absolute;top:323px;width:160px;height:130px;text-align:center;color:var(--white)}
.feature:nth-child(odd){background:var(--green)}
.feature:nth-child(even){background:var(--green-light)}
.feature-icon{position:absolute;left:39px;top:-41px;width:82px;height:82px;border-radius:50%;background:var(--white);border:3px solid var(--green);display:flex;align-items:center;justify-content:center}
.feature h3{position:absolute;top:51px;width:100%;font-size:12.5px;font-weight:500}
.feature p{position:absolute;top:70px;left:10px;right:10px;font-size:9.5px;line-height:11px;color:#eef6e2}
.feature .plus{position:absolute;left:70px;bottom:0;width:21px;height:20px;background:var(--orange);border:2px solid var(--white);border-bottom:0;display:flex;align-items:center;justify-content:center}

/* section titles */
.section-title{position:absolute;left:113px;font-size:14px;font-weight:400;padding-left:5px;border-left:2px solid var(--green);line-height:16px;letter-spacing:.2px}
.pager{position:absolute;display:flex;gap:1px}
.pager span{width:16px;height:15px;display:flex;align-items:center;justify-content:center}

/* trending */
.track{position:absolute;top:510px;width:147px}
.cover{width:147px;height:147px;border:5px solid var(--green)}
.cover.alt{border-color:var(--orange)}
.track p{margin-top:6px;font-size:8.6px;font-weight:700;font-style:italic;white-space:nowrap}
.track .actions{position:relative;height:23px;margin-top:5px;border-bottom:2px solid var(--green)}
.track .actions.muted{border-color:#aaa}
.btn-sm{position:absolute;top:1px;height:15px;font-size:8.5px;font-weight:500;color:var(--white);display:flex;align-items:center;justify-content:center}
.btn-share{left:2px;width:39px;background:var(--green)}
.btn-gift{right:2px;width:40px;background:var(--grey-btn)}

/* call to action */
.cta{position:absolute;left:113px;top:726px;width:640px;height:59px;background:var(--cream);border:1px solid var(--cream-line)}
.cta p{position:absolute;left:6px;top:20px;font-size:13.6px;color:#3a3a3a;white-space:nowrap}
.cta .btn{position:absolute;left:543px;top:14px;width:88px;height:28px;background:var(--green);color:var(--white);font-size:10px;font-weight:700;display:flex;align-items:center;justify-content:center}

/* categories */
.read-more{position:absolute;left:684px;top:815px;width:67px;height:20px;background:var(--orange-dark);font-size:8.5px;font-weight:700;color:#3a2200;display:flex;align-items:center;justify-content:center}
.rule{position:absolute;left:113px;top:845px;width:640px;height:1px;background:#eee}
.cat-col{position:absolute;top:852px;width:80px;list-style:none}
.cat-col li{position:relative;height:26.6px;border-bottom:1px solid #eee;font-size:9.3px;color:#444;padding-left:16px;display:flex;align-items:center;white-space:nowrap}
.cat-col li::before{content:"";position:absolute;left:0;top:8px;width:11px;height:11px;border-radius:50%;background:radial-gradient(circle,#fff 0 1.5px,#bbb 2px 100%)}
.cat-col li::after{content:"";position:absolute;right:0;top:10px;width:7px;height:7px;background:var(--green)}
.cat-col li.current{color:var(--green)}

/* footer */
.site-footer{position:absolute;left:0;top:1038px;width:821px;height:134px;background:var(--footer);border-top:2px solid var(--green);color:var(--white);font-family:"Lato",sans-serif}
.site-footer h4{position:absolute;top:12px;font-size:13px;font-weight:400;padding-bottom:5px;border-bottom:1px solid #555}
.quick-links{position:absolute;left:116px;top:38px;list-style:none}
.quick-links li{font-size:9px;line-height:14.4px;padding-left:8px;position:relative}
.quick-links li::before{content:"›";position:absolute;left:0;top:-1px}
.news-item{position:absolute;left:229px;width:160px}
.news-date{position:absolute;left:0;top:0;width:25px;text-align:center}
.news-date b{display:block;background:var(--green);font-size:10px;height:13px;line-height:13px}
.news-date i{display:block;background:#eee;color:#333;font-size:7px;font-style:normal;font-weight:700;height:9px;line-height:9px}
.news-item p{position:absolute;left:34px;top:-2px;font-size:8.6px;line-height:10.3px;width:125px}
.newsletter p{position:absolute;left:430px;top:37px;width:140px;font-size:8.4px;line-height:13px}
.email{position:absolute;left:430px;top:1108px;width:142px;height:17px;background:var(--white);font-size:7.5px;font-style:italic;color:#999;padding:4px 5px}
.subscribe{position:absolute;left:430px;top:1134px;width:72px;height:19px;background:var(--green);font-family:"Lato",sans-serif;font-size:10px;font-weight:700;color:var(--white);display:flex;align-items:center;justify-content:center}
.footer-brand{position:absolute;left:622px;top:1080px;display:flex;align-items:center;gap:5px;color:var(--white)}
.footer-brand .brand-dot{width:24px;height:24px}
.footer-brand span{font-family:"Lato",sans-serif;font-weight:700;font-size:25px}
.social{position:absolute;left:642px;top:1133px;display:flex;gap:7px}
.social span{width:15px;height:15px;border-radius:50%;background:#555}
.social span:nth-child(2){background:var(--green)}
.copyright{position:absolute;left:0;top:1172px;width:821px;height:28px;background:var(--footer-deep);color:#ddd;font-size:8.5px;display:flex;align-items:center;justify-content:center}
</style>
</head>
<body>

<header class="site-header">
  <div class="brand"><span class="brand-dot"></span><span class="brand-name">Quarry</span></div>
  <nav class="main-nav">
    <a class="active" href="#">HOME</a>
    <a href="#" style="left:440px">SERVICES</a>
    <a href="#" style="left:508px">TIMETABLE</a>
    <a href="#" style="left:582px">NEWS</a>
    <a href="#" style="left:632px">FEATURES</a>
    <a href="#" style="left:698px">CONTACTS</a>
  </nav>
  <div class="account">LOGIN &nbsp;|&nbsp; SIGNUP</div>
</header>

<div class="hero" role="img" aria-label="Young woman in headphones and sunglasses giving a thumbs up while holding a music player, city buildings behind"></div>

<section class="features abs" style="left:113px;top:0">
  <div class="feature" style="left:0">
    <div class="feature-icon"><svg width="34" height="34" viewBox="0 0 24 24" fill="var(--orange)"><path d="M9 3v12.3A3.5 3.5 0 1 0 11 18V8h9v5.3A3.5 3.5 0 1 0 22 16V3z"/></svg></div>
    <h3>UPLOAD MUSIC &amp; AUDIO</h3>
    <p>Lorem Ipsum is simply dummy text of the printing.</p>
    <span class="plus"><svg width="11" height="11"><path d="M4 0h3v4h4v3H7v4H4V7H0V4h4z" fill="#fff"/></svg></span>
  </div>
  <div class="feature" style="left:160px">
    <div class="feature-icon"><svg width="40" height="40" viewBox="0 0 24 24" fill="none" stroke="var(--orange)" stroke-width="2.4"><path d="M3 15v-3a9 9 0 0 1 18 0v3"/><rect x="2" y="14" width="5" height="7" rx="1.5" fill="var(--orange)"/><rect x="17" y="14" width="5" height="7" rx="1.5" fill="var(--orange)"/></svg></div>
    <h3>LISTEN &amp; DISCOVER</h3>
    <p>Lorem Ipsum is simply dummy text of the printing fdsjoid.</p>
    <span class="plus"><svg width="11" height="11"><path d="M4 0h3v4h4v3H7v4H4V7H0V4h4z" fill="#fff"/></svg></span>
  </div>
  <div class="feature" style="left:320px">
    <div class="feature-icon"><svg width="40" height="40" viewBox="0 0 24 24" fill="var(--orange)"><circle cx="10" cy="7" r="4.5"/><path d="M1 21c0-5 4-8 9-8s9 3 9 8z"/><circle cx="17" cy="14" r="3"/><path d="M12 22c0-3 2-5 5-5s5 2 5 5z"/></svg></div>
    <h3>CONNECT</h3>
    <p>Lorem Ipsum is simply dummy text of the printing.</p>
    <span class="plus"><svg width="11" height="11"><path d="M4 0h3v4h4v3H7v4H4V7H0V4h4z" fill="#fff"/></svg></span>
  </div>
  <div class="feature" style="left:480px">
    <div class="feature-icon"><svg width="40" height="40" viewBox="0 0 24 24" fill="var(--orange)" stroke="var(--orange)" stroke-width="2"><path d="M5 6l7 6M19 5l-7 7M12 12l7 6M12 12l-8 7"/><circle cx="12" cy="12" r="3.5"/><circle cx="5" cy="5" r="2.5"/><circle cx="19" cy="5" r="2.5"/><circle cx="19" cy="19" r="2.5"/><circle cx="4" cy="19" r="2.5"/></svg></div>
    <h3>SHARE</h3>
    <p>Lorem Ipsum is simply dummy text of the printing fdsjoid.</p>
    <span class="plus"><svg width="11" height="11"><path d="M4 0h3v4h4v3H7v4H4V7H0V4h4z" fill="#fff"/></svg></span>
  </div>
</section>

<h2 class="section-title" style="top:483px">TRENDING MUSIC &amp; AUDIO</h2>
<div class="pager" style="left:719px;top:483px">
  <span style="background:#ccc"><svg width="6" height="8"><path d="M5 0L1 4l4 4" stroke="#fff" fill="none"/></svg></span>
  <span style="background:var(--green)"><svg width="6" height="8"><path d="M1 0l4 4-4 4" stroke="#fff" fill="none"/></svg></span>
</div>

<article class="track" style="left:113px">
  <div class="cover" role="img" aria-label="Black and white album cover of a singer" style="background:linear-gradient(#6a6a6a,#1c1c1c)"></div>
  <p>Lorem ipsum dolor sfgjit rem Ipsumis</p>
  <div class="actions"><span class="btn-sm btn-share">SHARE</span><span class="btn-sm btn-gift">GIFT</span></div>
</article>
<article class="track" style="left:277px">
  <div class="cover alt" role="img" aria-label="Dark album cover with copper lettering and a play button" style="background:radial-gradient(circle,#7a4a30,#120c0a 70%)"></div>
  <p>Lorem ipsum dolor sfgjit rem Ipsumis</p>
  <div class="actions muted"><span class="btn-sm btn-share">SHARE</span><span class="btn-sm btn-gift">GIFT</span></div>
</article>
<article class="track" style="left:440px">
  <div class="cover" role="img" aria-label="Bright pink and white greatest hits album cover" style="background:linear-gradient(135deg,#e2238c,#f4f0f2 55%,#e2238c)"></div>
  <p>Lorem ipsum dolor sfgjit rem Ipsumis</p>
  <div class="actions"><span class="btn-sm btn-share">SHARE</span><span class="btn-sm btn-gift">GIFT</span></div>
</article>
<article class="track" style="left:604px">
  <div class="cover" role="img" aria-label="Dark gold fantasy metal album artwork" style="background:radial-gradient(circle at 50% 40%,#b08a3a,#3b2810 75%)"></div>
  <p>Lorem ipsum dolor sfgjit rem Ipsumis</p>
  <div class="actions"><span class="btn-sm btn-share">SHARE</span><span class="btn-sm btn-gift">GIFT</span></div>
</article>

<section class="cta">
  <p>So are you ready to discover new music and sounds and share them with the world?</p>
  <span class="btn">SIGN UP NOW</span>
</section>

<h2 class="section-title" style="top:817px">MUSIC CATEGORIES</h2>
<span class="read-more">READ MORE</span>
<div class="rule"></div>

<ul class="cat-col" style="left:113px"><li class="current">Acoustic</li><li>Music-Pack</li><li>Drum'n' Bass</li><li>Alternative</li><li>Eurodance</li><li>Ambient</li></ul>
<ul class="cat-col" style="left:220px"><li>Acoustic</li><li>Music-Pack</li><li>Drum'n' Bass</li><li>Alternative</li><li>Eurodance</li><li>Ambient</li></ul>
<ul class="cat-col" style="left:329px"><li>Acoustic</li><li>Music-Pack</li><li>Drum'n' Bass</li><li>Alternative</li><li>Eurodance</li><li>Ambient</li></ul>
<ul class="cat-col" style="left:439px"><li>Acoustic</li><li>Music-Pack</li><li>Drum'n' Bass</li><li>Alternative</li><li>Eurodance</li><li>Ambient</li></ul>
<ul class="cat-col" style="left:552px"><li>Acoustic</li><li>Music-Pack</li><li>Drum'n' Bass</li><li>Alternative</li><li>Eurodance</li><li>Ambient</li></ul>
<ul class="cat-col" style="left:668px"><li>Acoustic</li><li>Music-Pack</li><li>Drum'n' Bass</li><li>Alternative</li><li>Eurodance</li><li>Ambient</li></ul>

<footer class="site-footer">
  <h4 style="left:113px;width:68px">Quick Links</h4>
  <ul class="quick-links"><li>Home</li><li>Services</li><li>Timetable</li><li>News</li><li>Features</li><li>Contact Us</li></ul>

  <h4 style="left:229px;width:156px">News Updates</h4>
  <div class="pager" style="left:362px;top:15px">
    <span style="background:var(--green);width:11px;height:11px"><svg width="5" height="7"><path d="M4 0L1 3.5 4 7" stroke="#fff" fill="none"/></svg></span>
    <span style="background:var(--green);width:11px;height:11px"><svg width="5" height="7"><path d="M1 0l3 3.5L1 7" stroke="#fff" fill="none"/></svg></span>
  </div>
  <div class="news-item" style="top:44px"><div class="news-date"><b>12</b><i>NOV</i></div><p><strong>Vero eros accumsaet odio</strong><br>quis nostrud exetiperj suscipit nisl ut aliquip ex ea commod</p></div>
  <div class="news-item" style="top:92px"><div class="news-date"><b>20</b><i>NOV</i></div><p><strong>Vero eros accumsaet odio</strong><br>quis nostrud exetiperj suscipit nisl ut aliquip ex ea commod</p></div>

  <div class="newsletter"><h4 style="left:430px;width:140px">Newsletter Sign Up</h4><p>Lorem ipsudolor sit coec adipiscing elitsite amet</p></div>
</footer>
<div class="email">Email Address</div>
<span class="subscribe">SUBSCRIBE</span>
<div class="footer-brand"><span class="brand-dot"></span><span>Quarry</span></div>
<div class="social"><span></span><span></span><span></span><span></span></div>

<div class="copyright">© 2014&nbsp;<strong>QuarryMusic</strong>. All Rights Reserved.</div>

</body>
</html>
```